Web Design Project

We are looking for a web page (home) page design for a website that offers Virtual Internet Marketing services.

The Company is called Kestrel Marketing, the services we provide are as follows:

Web Design
Social Media Management
SEO/PPC Traffic
Display
Mobile Apps
On & Offline Marketing Services

We see so many web marketing companies that struggle to produce their own great designs and call to actions. 99% of web companies do not understand marketing, so how can they help their customers drive traffic and produce sales!

We require a design that is professional yet fresh and funky! Our goal with the home page is to help prospects understand that our core business is to help them succeed and make more money, by utilising our on and offline marketing experience. We also offer done for you solutions which include - websites, design, traffic, email campaigns etc.

Included should be obvious call to actions to view our services and get our free guide/video

- A clear value proposition that identifies target audience (those that are struggling to make the web work for them)

- Easy to use navigation

We need to include an optin form where we exchange a free training guide or video series in return for an email address, above the fold to the right of the page!

We like the following to provide you with ideas:

http://www.plankhaven.com/
http://www.morvale.co.uk/
http://www.brindletopic.com/
http://www.wemplo.co.uk/ (quite like but too jumbled - too much going on)

Colours are optional, however fresh, vibrant and professional looking.

The final design should be easy on the eye, not lead to any confusion as to what we do and be simple to navigate.

Industry/Entity Type

Marketing

Requirements
Must have
• Optin form
Footer section
showcase of services offered.

```html
<!DOCTYPE html>
<html lang="en">
<head>
<meta charset="utf-8">
<title>Kestrel Marketing</title>
<link rel="stylesheet" href="https://fonts.googleapis.com/css2?family=Open+Sans:ital,wght@0,400;0,600;0,700;1,700;1,800&family=Kaushan+Script&family=Mr+Dafoe&display=swap">
<style>
:root{
  --cyan:#16b3e6;
  --cyan-deep:#0a8fc8;
  --ink:#2b2b2b;
  --dark:#1f1f1f;
  --darker:#161616;
  --grey-bg:#e9e9e9;
  --text:#6d6d6d;
  --white:#ffffff;
  --orange:#f07c1e;
  --line:#cfcfcf;
}
*{box-sizing:border-box;margin:0;padding:0}
html,body{width:717px;height:1200px;overflow:hidden}
body{font-family:"Open Sans",Arial,sans-serif;color:var(--ink);background:var(--white);position:relative}
.page{position:relative;width:717px;height:1200px}

/* header */
.site-header{position:absolute;top:0;left:0;width:717px;height:70px;background:var(--white)}
.brand{position:absolute;left:22px;top:12px;display:flex;align-items:center;gap:8px}
.brand-mark{width:32px;height:32px;background:var(--cyan);border-radius:4px}
.brand-name{font-weight:700;font-size:17px;color:var(--ink);line-height:1}
.contact-bar{position:absolute;right:22px;top:8px;font-size:8px;color:var(--text)}
.main-nav{position:absolute;right:20px;top:36px;display:flex;gap:3px}
.main-nav a{display:block;font-size:10px;font-weight:600;color:var(--ink);text-decoration:none;padding:5px 10px;border-radius:2px}
.main-nav a.active{background:var(--dark);color:var(--white)}

/* hero */
.hero{position:absolute;top:70px;left:0;width:717px;height:300px;background:linear-gradient(180deg,#2cc3ef 0%,var(--cyan) 45%,var(--cyan-deep) 100%);text-align:center;overflow:hidden}
.hero-title{margin-top:22px;font-size:26px;font-weight:800;font-style:italic;color:var(--white);letter-spacing:-.3px}
.hero-sub{margin-top:2px;font-family:"Kaushan Script",cursive;font-size:14px;color:#d9f4ff}
.hero-visual{position:absolute;left:150px;top:80px;width:420px;height:220px;border-radius:4px 4px 0 0;background:linear-gradient(160deg,#eef3f5 0%,#c9d6dc 55%,#9fb3bd 100%)}

/* welcome */
.welcome{position:absolute;top:370px;left:0;width:717px;height:60px;background:var(--dark);text-align:center}
.slider-dots{padding-top:6px;display:flex;justify-content:center;gap:5px}
.slider-dots span{width:7px;height:7px;border-radius:50%;background:#777}
.slider-dots span.on{background:var(--white)}
.welcome h2{margin-top:10px;font-size:17px;font-weight:600;color:var(--white)}
.welcome h2 em{font-style:normal;color:var(--cyan)}
.intro{position:absolute;top:430px;left:0;width:717px;height:60px;background:var(--darker);padding:9px 90px 0;text-align:center;font-size:8.5px;line-height:13px;color:#8a8a8a}

/* services */
.services{position:absolute;top:490px;left:0;width:717px;height:300px;background:var(--grey-bg)}
.section-title{text-align:center;padding-top:26px;font-size:21px;font-weight:600;color:var(--ink)}
.section-title em{font-style:normal;color:var(--cyan)}
.services-rule{width:520px;height:1px;background:var(--line);margin:10px auto 0}
.service-list{position:absolute;top:80px;left:60px;width:597px;display:flex;justify-content:space-between}
.service{width:170px;text-align:center}
.service svg{display:block;margin:0 auto;height:56px}
.service h3{margin-top:12px;font-size:13px;font-weight:600;color:var(--cyan)}
.service p{margin-top:5px;font-size:8px;line-height:11px;color:var(--text)}
.btn-more{display:inline-block;margin-top:8px;font-size:8px;color:var(--white);background:var(--dark);padding:3px 10px;border-radius:2px}
.slide-arrow{position:absolute;top:155px;width:18px;height:18px;border-radius:50%;background:#bdbdbd}
.slide-arrow svg{display:block}
.slide-arrow.prev{left:12px}.slide-arrow.next{right:12px}

/* testimonials */
.testimonials{position:absolute;top:790px;left:0;width:717px;height:115px;background:var(--grey-bg)}
.testimonials-tab{position:absolute;left:50%;top:2px;transform:translateX(-50%);background:var(--cyan);color:var(--white);font-size:13px;font-weight:600;padding:4px 14px;border-radius:2px;display:flex;align-items:center;gap:6px}
.testimonials-tab i{width:11px;height:11px;background:var(--white);border-radius:2px}
.quote-box{position:absolute;left:40px;top:26px;width:637px;height:82px;background:var(--white);border:1px solid #dcdcdc;padding:10px 14px;font-size:8px;line-height:12px;color:var(--text)}
.quote-author{position:absolute;right:16px;bottom:4px;font-family:"Mr Dafoe",cursive;font-size:15px;color:#444}

/* clients */
.clients{position:absolute;top:905px;left:0;width:717px;height:50px;background:var(--white);display:flex;align-items:center;justify-content:space-between;padding:0 28px}
.clients-count{font-size:8px;font-weight:700;color:#777;line-height:10px}
.clients-count b{color:var(--cyan)}
.client-badge{width:52px;height:14px;background:#bfbfbf;border-radius:2px}

/* footer */
.site-footer{position:absolute;top:955px;left:0;width:717px;height:220px;background:var(--dark);padding:20px 30px 0;display:flex;gap:26px}
.footer-col h4{font-size:11px;font-weight:600;color:var(--cyan);margin-bottom:8px}
.footer-col ul{list-style:none}
.footer-col li{font-size:8px;line-height:15px;color:#a8a8a8}
.col-sitemap{width:90px}.col-services{width:120px}.col-social{width:110px}.col-contact{width:215px}
.col-social li{display:flex;align-items:center;gap:5px}
.col-social li i{width:10px;height:10px;background:#555;border-radius:2px}
.col-contact p{font-size:8px;line-height:12px;color:#a8a8a8}
.optin{margin-top:10px;display:flex}
.optin span{flex:1;height:20px;background:var(--white);font-size:8px;color:#999;padding:5px 6px}
.optin b{background:var(--orange);color:var(--white);font-size:9px;font-weight:700;padding:5px 12px}
.copyright{position:absolute;top:1175px;left:0;width:717px;height:25px;background:var(--darker);text-align:center;font-size:8px;line-height:25px;color:#777}
</style>
</head>
<body>
<div class="page">

<header class="site-header">
  <div class="brand"><span class="brand-mark"></span><span class="brand-name">Kestrel Marketing</span></div>
  <div class="contact-bar">Phone: +44 (0)20 7946 0321 &nbsp;|&nbsp; Email: hello@kestrelmarketing.com</div>
  <nav class="main-nav">
    <a class="active" href="#">Home</a><a href="#">About Us</a><a href="#">Services</a><a href="#">Cases</a><a href="#">Blogs</a><a href="#">Contact Us</a>
  </nav>
</header>

<section class="hero">
  <h1 class="hero-title">We Are Different to Most Web Design Agencies</h1>
  <p class="hero-sub">as our websites are designed by marketing experts who know exactly what it takes to look good</p>
  <div class="hero-visual" role="img" aria-label="Collage of website screenshots from client projects"></div>
</section>

<section class="welcome">
  <div class="slider-dots"><span class="on"></span><span></span><span></span><span></span></div>
  <h2>Welcome to <em>Kestrel Marketing</em></h2>
</section>
<p class="intro">There are many variations of passages of Lorem Ipsum available, but the majority have suffered alteration in some form, by injected humour, or randomised words which don't look even slightly believable. If you are going to use a passage of Lorem Ipsum, you need to be sure there isn't anything embarrassing hidden in the middle of text.</p>

<section class="services">
  <h2 class="section-title"><em>Our</em> Services</h2>
  <div class="services-rule"></div>
  <span class="slide-arrow prev"><svg width="18" height="18" viewBox="0 0 18 18"><path d="M10.5 5 6.5 9l4 4" fill="none" stroke="#fff" stroke-width="2"/></svg></span>
  <span class="slide-arrow next"><svg width="18" height="18" viewBox="0 0 18 18"><path d="M7.5 5l4 4-4 4" fill="none" stroke="#fff" stroke-width="2"/></svg></span>
  <div class="service-list">
    <div class="service">
      <svg viewBox="0 0 60 56" width="60"><g fill="#2b2b2b"><rect x="4" y="30" width="9" height="22"/><rect x="17" y="18" width="9" height="34"/><rect x="30" y="8" width="9" height="44"/><rect x="43" y="24" width="9" height="28"/></g><rect x="0" y="52" width="58" height="3" fill="#2b2b2b"/></svg>
      <h3>On &amp; Offline Marketing</h3>
      <p>Lorem Ipsum is simply dummy text of the printing and typesetting industry. Lorem Ipsum has been the industry's standard dummy text ever since the.</p>
      <span class="btn-more">Learn More</span>
    </div>
    <div class="service">
      <svg viewBox="0 0 34 56" width="34"><rect x="2" y="1" width="30" height="54" rx="5" fill="#2b2b2b"/><rect x="6" y="8" width="22" height="38" fill="#e9e9e9"/><circle cx="17" cy="50" r="2.5" fill="#e9e9e9"/></svg>
      <h3>Mobile App</h3>
      <p>Lorem Ipsum is simply dummy text of the printing and typesetting industry. Lorem Ipsum has been the industry's standard dummy text ever since the.</p>
      <span class="btn-more">Learn More</span>
    </div>
    <div class="service">
      <svg viewBox="0 0 66 56" width="66"><rect x="2" y="2" width="62" height="40" rx="3" fill="#2b2b2b"/><rect x="6" y="6" width="54" height="32" fill="#e9e9e9"/><rect x="28" y="42" width="10" height="8" fill="#2b2b2b"/><rect x="18" y="50" width="30" height="4" rx="1" fill="#2b2b2b"/></svg>
      <h3>Web Design</h3>
      <p>Lorem Ipsum is simply dummy text of the printing and typesetting industry. Lorem Ipsum has been the industry's standard dummy text ever since the.</p>
      <span class="btn-more">Learn More</span>
    </div>
  </div>
</section>

<section class="testimonials">
  <div class="testimonials-tab"><i></i>Testimonials</div>
  <blockquote class="quote-box">Lorem Ipsum is simply dummy text of the printing and typesetting industry. Lorem Ipsum has been the industry's standard dummy text ever since the 1500s, when an unknown printer took a galley of type and scrambled it to make a type specimen book. It has survived not only five centuries, but also the leap into electronic typesetting, remaining essentially unchanged. It was popularised in the 1960s with the release of sheets containing passages, and more recently with desktop publishing software.
    <cite class="quote-author">Daniel Hartwell</cite>
  </blockquote>
</section>

<section class="clients" aria-label="Client list">
  <div class="clients-count">OVER <b>300 HAPPY</b><br>CUSTOMERS WORLDWIDE</div>
  <span class="client-badge"></span><span class="client-badge"></span><span class="client-badge"></span><span class="client-badge"></span><span class="client-badge"></span><span class="client-badge"></span><span class="client-badge"></span>
</section>

<footer class="site-footer">
  <div class="footer-col col-sitemap">
    <h4>Site Map</h4>
    <ul><li>Home</li><li>About Us</li><li>Services</li><li>Cases</li><li>Blogs</li><li>Contact Us</li></ul>
  </div>
  <div class="footer-col col-services">
    <h4>Our Services</h4>
    <ul><li>Web Design</li><li>Social Media Management</li><li>SEO/PPC Traffic</li><li>Display</li><li>Mobile Apps</li><li>On &amp; Offline Marketing Services</li></ul>
  </div>
  <div class="footer-col col-social">
    <h4>Social Media</h4>
    <ul><li><i></i>Friends Page</li><li><i></i>Updates Feed</li><li><i></i>Video Channel</li><li><i></i>Pro Network</li><li><i></i>Photo Board</li></ul>
  </div>
  <div class="footer-col col-contact">
    <h4>Contact Us</h4>
    <p>Get our free training guide and video series sent straight to your inbox. Just enter your email address below.</p>
    <p>Phone: +44 (0)20 7946 0321<br>Email: hello@kestrelmarketing.com</p>
    <div class="optin"><span>Your email address</span><b>Join Now</b></div>
  </div>
</footer>
<div class="copyright">&copy; 2013 Kestrel Marketing. All Rights Reserved.</div>

</div>
</body>
</html>
```